Business card for a "family office" company

Please provide professional looking business card designs, incorporating the attached logo and below details. Harrowmere Holdings Pty Ltd is a family office / financial investment company. We are looking for a modern, professional and contemporary card design.

Industry/Entity Type

Finance

Contact Information for Business Card

Name: Dean Mollick
Title: Director
Company: Harrowmere Holdings Pty Ltd
Email: harrowdean@quillnet.example
Mobile: 0462 735 418
Address: 4/312 Barnaby Parade, Fernleigh Bay WA 6990, Australia

Requirements
Must have
• All details above and the logo. logo only on back side. incorporate colours of logo
Nice to have
• up to you
Should not have
• ?

```html
<!DOCTYPE html>
<html lang="en">
<head>
<meta charset="utf-8">
<title>Harrowmere Holdings – Business Card</title>
<link rel="stylesheet" href="https://fonts.googleapis.com/css2?family=Cinzel:wght@400;600&family=Marcellus+SC&display=swap">
<style>
  :root {
    --navy: #25266b;
    --navy-deep: #1c1d58;
    --paper: #ffffff;
    --paper-shade: #eef0f5;
    --stage: #2b2b2e;
    --ink-light: #e9eaf4;
  }
  * { box-sizing: border-box; margin: 0; padding: 0; }
  html, body { width: 1200px; height: 997px; overflow: hidden; }
  body {
    background: var(--stage);
    position: relative;
    font-family: "Marcellus SC", "Cinzel", serif;
  }
  .card {
    position: absolute;
    width: 540px;
    height: 310px;
    top: 343px;
    overflow: hidden;
    box-shadow: 0 12px 30px rgba(0,0,0,.45);
  }

  /* Back side */
  .card-back {
    left: 40px;
    background: var(--navy);
    display: flex;
    align-items: center;
    justify-content: center;
  }
  .brand {
    font-family: "Cinzel", serif;
    font-weight: 600;
    text-transform: uppercase;
    text-align: center;
    line-height: 1.15;
  }
  .card-back .brand {
    color: var(--paper);
    font-size: 40px;
    letter-spacing: 3px;
  }
  .card-back .brand .brand-sub {
    display: block;
    letter-spacing: 6px;
  }

  /* Front side */
  .card-front {
    left: 620px;
    background: linear-gradient(180deg, var(--paper) 0%, var(--paper-shade) 100%);
  }
  .front-brand {
    position: absolute;
    top: 0; left: 0; right: 0;
    height: 148px;
    display: flex;
    align-items: center;
    justify-content: center;
  }
  .front-brand .brand {
    color: var(--navy);
    font-size: 26px;
    letter-spacing: 2px;
  }
  .front-brand .brand .brand-sub {
    display: block;
    letter-spacing: 5px;
  }
  .band-rules {
    position: absolute;
    left: 0; top: 150px;
    width: 540px; height: 12px;
  }
  .contact-band {
    position: absolute;
    left: 0; right: 0;
    top: 164px; height: 102px;
    background: var(--navy);
  }
  .band-stripes {
    position: absolute;
    left: 0; top: 8px;
  }
  .holder {
    position: absolute;
    left: 60px; top: 42px;
    color: var(--ink-light);
  }
  .holder-name { font-size: 17px; letter-spacing: 1px; text-transform: uppercase; }
  .holder-title { font-size: 14px; margin-left: 28px; letter-spacing: .5px; }
  .band-divider {
    position: absolute;
    left: 246px; top: 14px;
    width: 1px; height: 72px;
    background: rgba(255,255,255,.55);
  }
  .contact-list {
    list-style: none;
    position: absolute;
    left: 262px; top: 14px;
    color: var(--ink-light);
    font-size: 12px;
    letter-spacing: .4px;
    white-space: nowrap;
  }
  .contact-list li { display: flex; align-items: center; gap: 7px; height: 20px; }
  .contact-list svg { width: 13px; height: 13px; flex: none; }
  .address {
    position: absolute;
    left: 0; right: 0; bottom: 0;
    height: 44px;
    display: flex;
    align-items: center;
    justify-content: center;
    color: var(--navy);
    font-size: 14.5px;
    letter-spacing: .6px;
    white-space: nowrap;
  }
</style>
</head>
<body>

  <section class="card card-back" aria-label="Card back">
    <div class="brand">Harrowmere<span class="brand-sub">Holdings</span></div>
  </section>

  <section class="card card-front" aria-label="Card front">
    <div class="front-brand">
      <div class="brand">Harrowmere<span class="brand-sub">Holdings</span></div>
    </div>

    <svg class="band-rules" viewBox="0 0 540 12" aria-hidden="true">
      <rect x="0" y="0" width="540" height="3" fill="var(--navy)"/>
      <rect x="0" y="7" width="540" height="3" fill="var(--navy)"/>
    </svg>

    <div class="contact-band">
      <svg class="band-stripes" width="74" height="14" viewBox="0 0 74 14" aria-hidden="true">
        <rect x="0" y="0" width="74" height="2" fill="#fff"/>
        <rect x="0" y="5" width="74" height="2" fill="#fff"/>
        <rect x="0" y="10" width="74" height="2" fill="#fff"/>
      </svg>
      <div class="holder">
        <div class="holder-name">Dean Mollick</div>
        <div class="holder-title">Director</div>
      </div>
      <div class="band-divider"></div>
      <ul class="contact-list">
        <li>
          <svg viewBox="0 0 14 14" aria-hidden="true">
            <circle cx="7" cy="7" r="7" fill="#fff"/>
            <path d="M4 5.2c0-.7.6-1.2 1.2-1.2h3.6c.6 0 1.2.5 1.2 1.2v.6H8.4V5H5.6v.8H4z M4.6 6.6h4.8l.6 3.4H4z" fill="var(--navy)"/>
          </svg>
          0462 735 418
        </li>
        <li>
          <svg viewBox="0 0 14 14" aria-hidden="true">
            <circle cx="7" cy="7" r="7" fill="#fff"/>
            <rect x="3.5" y="4.5" width="7" height="5" fill="none" stroke="var(--navy)" stroke-width="1"/>
            <path d="M3.5 4.5 7 7.4 10.5 4.5" fill="none" stroke="var(--navy)" stroke-width="1"/>
          </svg>
          harrowdean@quillnet.example
        </li>
      </ul>
    </div>

    <p class="address">4/312 Barnaby Parade, Fernleigh Bay WA 6990, Australia</p>
  </section>

</body>
</html>
```